New Business Card Design for Engineering and Surveying Company

We need a new design template for our business cards. We are a civil engineering, land surveying and pipeline integrity business. Please see brqholt.com for details. We need a bold, new business card design to complement our rebranding and marketing program. We have anew logo and attached vectro file. Please find additional details below. I am available to answer any questions.

Target Market(s)

Contractors, business owners, oil companies

Contact Information for Business Card

Needs to be customizable for different people (name, title, cell)

Font styles to use
Sans Serif
Other font styles liked:
• See eps file

Requirements
Must have
• Example Information:
Derek Fannaby

T:409-555-0187
M: 202-555-0143
dfannaby@brqholt.com

Address: 1870 Corvane Parkway, Beaumont, Texas 77701
Email: dfanbagy@brqholt.com
Website: www.brqholt.com
Nice to have
• I would like the back of the card to have the logo on a bold background with the text below:

[logo]
ROLAND FANNABY & ASSOCIATES
CIVIL ENGINEERING | LAND SURVEYING | PIPELINE INTEGRITY

The reverse side should have the contact information for the person (example above), a smaller version of the logo and a graphic

```html
<!DOCTYPE html>
<html lang="en">
<head>
<meta charset="utf-8">
<title>Roland Fannaby &amp; Associates – Business Card</title>
<link rel="stylesheet" href="https://fonts.googleapis.com/css2?family=Montserrat:wght@500;600;800&family=Roboto:wght@400;500&display=swap">
<style>
  :root {
    --backdrop: #3b3b3d;
    --card: #1f1f21;
    --white: #ffffff;
    --soft-white: #e6e6e6;
    --red: #e0242f;
    --blue: #2b3fa0;
    --rule: #8a8a8e;
  }
  * { box-sizing: border-box; margin: 0; padding: 0; }
  html, body { width: 799px; height: 1200px; overflow: hidden; }
  body {
    background: var(--backdrop);
    font-family: "Montserrat", sans-serif;
    color: var(--white);
  }
  .card {
    position: absolute;
    left: 60px;
    width: 680px;
    height: 389px;
    background: var(--card);
    border-radius: 4px;
    box-shadow: 0 14px 34px rgba(0,0,0,0.45);
    overflow: hidden;
  }
  .card--front { top: 150px; }
  .card--back { top: 650px; }

  .brand-mark {
    display: flex;
    align-items: center;
    gap: 18px;
  }
  .brand-mark__square {
    width: 34px;
    height: 34px;
    background: var(--red);
  }
  .brand-mark__name {
    font-family: "Montserrat", sans-serif;
    font-weight: 800;
    color: var(--white);
    line-height: 1;
    letter-spacing: 2px;
  }

  /* Front */
  .card--front .brand-mark {
    position: absolute;
    left: 110px;
    top: 80px;
  }
  .card--front .brand-mark__name { font-size: 120px; }
  .company-name {
    position: absolute;
    left: 110px;
    top: 218px;
    font-weight: 600;
    font-size: 22px;
    letter-spacing: 1px;
    color: var(--white);
  }
  .services {
    position: absolute;
    left: 0;
    right: 0;
    bottom: 42px;
    text-align: center;
    font-weight: 500;
    font-size: 15px;
    letter-spacing: 0.5px;
    color: var(--soft-white);
  }
  .services__sep { color: var(--red); margin: 0 10px; }

  /* Back */
  .card--back .brand-mark {
    position: absolute;
    left: 50px;
    top: 150px;
  }
  .card--back .brand-mark__name { font-size: 82px; }
  .divider {
    position: absolute;
    left: 340px;
    top: 50px;
    width: 1px;
    height: 290px;
    background: var(--rule);
  }
  .contact {
    position: absolute;
    left: 378px;
    top: 62px;
    font-family: "Roboto", sans-serif;
  }
  .contact__name {
    font-weight: 500;
    font-size: 25px;
    color: var(--blue);
  }
  .contact__title {
    font-size: 16px;
    color: var(--white);
    margin-top: 2px;
    margin-bottom: 20px;
  }
  .contact__list { list-style: none; }
  .contact__item {
    display: flex;
    align-items: center;
    gap: 12px;
    font-size: 17px;
    line-height: 27px;
    color: var(--white);
  }
  .contact__icon { width: 15px; height: 15px; flex: none; }
  .contact__address {
    margin-top: 4px;
    font-size: 17px;
    line-height: 25px;
    color: var(--white);
  }
</style>
</head>
<body>

<section class="card card--front" aria-label="Card front">
  <div class="brand-mark">
    <span class="brand-mark__square"></span>
    <span class="brand-mark__name">RFA</span>
  </div>
  <p class="company-name">ROLAND FANNABY &amp; ASSOCIATES</p>
  <p class="services">CIVIL ENGINEERING<span class="services__sep">|</span>LAND SURVEYING<span class="services__sep">|</span>PIPELINE INTEGRITY</p>
</section>

<section class="card card--back" aria-label="Card back">
  <div class="brand-mark">
    <span class="brand-mark__square"></span>
    <span class="brand-mark__name">RFA</span>
  </div>
  <div class="divider"></div>
  <div class="contact">
    <p class="contact__name">Derek Fannaby</p>
    <p class="contact__title">Chief Executive Officer</p>
    <ul class="contact__list">
      <li class="contact__item">
        <svg class="contact__icon" viewBox="0 0 16 16"><path fill="#e0242f" d="M3 1h3l1.5 4-2 1.5a9 9 0 0 0 4 4L11 8.5l4 1.5v3a2 2 0 0 1-2 2A12 12 0 0 1 1 3a2 2 0 0 1 2-2z"/></svg>
        409-555-0187
      </li>
      <li class="contact__item">
        <svg class="contact__icon" viewBox="0 0 16 16"><rect x="4" y="1" width="8" height="14" rx="1.5" fill="#e0242f"/><rect x="5.5" y="3" width="5" height="8" fill="#1f1f21"/></svg>
        202-555-0143
      </li>
      <li class="contact__item">
        <svg class="contact__icon" viewBox="0 0 16 16"><rect x="1" y="3" width="14" height="10" rx="1" fill="#e0242f"/><path d="M1.5 3.5 8 9l6.5-5.5" fill="none" stroke="#1f1f21" stroke-width="1.3"/></svg>
        dfannaby@brqholt.com
      </li>
      <li class="contact__item">
        <svg class="contact__icon" viewBox="0 0 16 16"><circle cx="8" cy="8" r="7" fill="#e0242f"/><path d="M1 8h14M8 1c-3 3-3 11 0 14M8 1c3 3 3 11 0 14" fill="none" stroke="#1f1f21" stroke-width="1"/></svg>
        www.brqholt.com
      </li>
    </ul>
    <p class="contact__address">1870 Corvane Parkway,<br>Beaumont, Texas 77701</p>
  </div>
</section>

</body>
</html>
```